Business Card cabinets and cabinets components making company.

the card should be formal and interesting at the same time. The main colors will be black and white.

Font styles to use
Sans Serif

Colors

Designer to choose only greyscale colors for use in the design.

Requirements
Must have
• At least must have the followings:
office phone
cell phone
address
position
name
email
web

```html
<!DOCTYPE html>
<html lang="en">
<head>
<meta charset="utf-8">
<title>Planeline business card</title>
<link href="https://fonts.googleapis.com/css2?family=Work+Sans:wght@400;500;700&display=swap" rel="stylesheet">
<style>
  :root {
    --backdrop: #1c1c1c;
    --card-dark: #141414;
    --card-light: #ffffff;
    --ink: #1e1e1e;
    --ink-soft: #3a3a3a;
    --paper-text: #ffffff;
  }
  * { margin: 0; padding: 0; box-sizing: border-box; }
  html, body {
    width: 1200px; height: 930px; overflow: hidden;
    background: var(--backdrop);
    font-family: "Work Sans", sans-serif;
  }
  .stage { position: relative; width: 1200px; height: 930px; }

  .card {
    position: absolute;
    width: 560px; height: 340px;
    border-radius: 18px;
    overflow: hidden;
  }
  .card-back {
    left: 60px; top: 110px;
    background: var(--card-dark);
    display: flex; align-items: center; justify-content: center;
  }
  .card-front {
    left: 580px; top: 470px;
    background: var(--card-light);
    color: var(--ink);
  }

  .brand {
    font-family: "Work Sans", sans-serif;
    font-weight: 700;
    letter-spacing: -0.5px;
    display: flex; align-items: center; gap: 12px;
    line-height: 1;
  }
  .brand-mark { display: block; width: 0.7em; height: 0.7em; }
  .card-back .brand { color: var(--paper-text); font-size: 64px; }
  .card-back .brand-mark { background: var(--paper-text); }
  .card-front .brand {
    position: absolute; right: 40px; top: 40px;
    color: var(--ink); font-size: 42px;
  }
  .card-front .brand-mark { background: var(--ink); }

  .contact {
    position: absolute; left: 34px; bottom: 26px;
    font-size: 13.5px; line-height: 1.4; color: var(--ink-soft);
  }
  .edge-tab {
    position: absolute; left: -34px; top: 2px;
    width: 8px; height: 36px; background: var(--ink);
  }
  .person-name { font-size: 17px; font-weight: 500; letter-spacing: 0.5px; color: var(--ink); }
  .person-role { margin-bottom: 8px; }
  .address { margin-bottom: 6px; }
  .contact-list { list-style: none; }
  .contact-list li { display: flex; align-items: center; gap: 8px; }
  .contact-list svg { width: 11px; height: 11px; flex: none; }
</style>
</head>
<body>
<main class="stage">
  <section class="card card-back" aria-label="Card back">
    <div class="brand"><span class="brand-mark"></span>Planeline</div>
  </section>

  <section class="card card-front" aria-label="Card front">
    <div class="brand"><span class="brand-mark"></span>Planeline</div>
    <div class="contact">
      <span class="edge-tab"></span>
      <p class="person-name">DANIEL REYES</p>
      <p class="person-role">Director</p>
      <p class="address">2215 Birchwood Court<br>Nashville, TN 37203</p>
      <ul class="contact-list">
        <li>
          <svg viewBox="0 0 12 12" aria-hidden="true"><path d="M2.5 1 L4.5 1 L5.2 3.6 L4 4.6 Q5.2 7 7.4 8 L8.4 6.8 L11 7.5 L11 9.5 Q10 11 8 10.8 Q2 9.5 1 3.5 Q1 1.6 2.5 1Z" fill="currentColor"/></svg>
          +330 5812-4409
        </li>
        <li>
          <svg viewBox="0 0 12 12" aria-hidden="true"><rect x="3" y="0.8" width="6" height="10.4" rx="1.2" fill="none" stroke="currentColor" stroke-width="1.3"/><circle cx="6" cy="9.3" r="0.7" fill="currentColor"/></svg>
          +330 5812-4401
        </li>
        <li>
          <svg viewBox="0 0 12 12" aria-hidden="true"><rect x="0.8" y="2.2" width="10.4" height="7.6" rx="1" fill="none" stroke="currentColor" stroke-width="1.2"/><path d="M1 2.6 L6 6.6 L11 2.6" fill="none" stroke="currentColor" stroke-width="1.2"/></svg>
          hello@planeline.com
        </li>
        <li>
          <svg viewBox="0 0 12 12" aria-hidden="true"><circle cx="6" cy="6" r="5" fill="none" stroke="currentColor" stroke-width="1.1"/><ellipse cx="6" cy="6" rx="2.2" ry="5" fill="none" stroke="currentColor" stroke-width="1"/><path d="M1 6 H11" stroke="currentColor" stroke-width="1"/></svg>
          www.planeline.com
        </li>
      </ul>
    </div>
  </section>
</main>
</body>
</html>
```